Belvo - Helping to Deliver Excellence in Aged Care

We are a new company based in Sydney, Australia. We have developed a state-of-the-art app for communication between aged care facilities and families.

Belvo has been developed for facilities to augment the best possible care by providing easy, safe and secure communication for families to stay in touch with their loved ones.
Updates

the website needs to be designed so we can add functionality including multilingual support. display in different languages.we also require enquiry and email/data base function. we want it simple and clean so its responsive. the target audience will be 40+ in age. there will be a video on home page. would like to start with 6 pages/ subjects -homepage -about us -our solution -demonstration page, this will be a page that contains videos of people using our product -customer testimonials -contact us

Target Market(s)

Aged care facilities.
Families (over 40’s age group) who are looking for a facility for their loved ones.

Number of Pages Required

5+ page

Font styles to use
Sans Serif

Colors
faa54b
ffffff
0255a3

Requirements
Must have
• - Our corporate colour is #EE8811.
• - If you're using stock photography, please use corvena stock photos as we have a license for their photos.
• - The design needs to be responsive (mobile and desktop)
• -White space on each page
Nice to have
• -need to leave a place for a future animation video to be added in on the home tab
Should not have
• we don't want flash technology

```html
<!DOCTYPE html>
<html lang="en">
<head>
<meta charset="utf-8">
<title>Belvo - Helping to Deliver Excellence in Aged Care</title>
<link href="https://fonts.googleapis.com/css2?family=Poppins:wght@300;400;500;600;700&display=swap" rel="stylesheet">
<style>
:root{
  --orange:#f7931e;
  --orange-soft:#faa54b;
  --ink:#1d2430;
  --text:#5a6270;
  --muted:#9aa0aa;
  --line:#e3e6ea;
  --nav:#1f1f1f;
  --feature-bg:#eef5fb;
  --footer:#0f1f33;
  --blue:#0255a3;
  --white:#ffffff;
}
*{margin:0;padding:0;box-sizing:border-box}
html,body{width:1200px;height:3805px;overflow:hidden}
body{font-family:'Poppins',sans-serif;color:var(--text);background:var(--white);position:relative}
.abs{position:absolute}
section,header,footer,nav{position:absolute;left:0;width:1200px}

/* top bar */
.topbar{top:0;height:30px;font-size:11px;color:var(--text)}
.topbar span{position:absolute;top:8px}
.topbar b{color:var(--ink);font-weight:600}
.lang{left:1090px;display:flex;align-items:center;gap:5px}
.lang i{display:inline-block;width:14px;height:10px;background:var(--blue);border-radius:2px}

/* header */
.site-header{top:30px;height:66px;border-top:1px solid var(--line)}
.brand{position:absolute;display:flex;align-items:center;gap:8px;font-weight:600;color:var(--orange)}
.brand i{display:block;border-radius:50%;border:3px solid var(--orange)}
.site-header .brand{left:38px;top:14px;font-size:30px}
.site-header .brand i{width:30px;height:30px}
.phone-block{left:590px;top:13px;display:flex;gap:10px;align-items:center}
.icon-circle{border-radius:50%;background:var(--orange);display:flex;align-items:center;justify-content:center;flex:none}
.phone-block .icon-circle{width:34px;height:34px}
.phone-block small{display:block;color:var(--orange);font-size:10px;line-height:12px}
.phone-block strong{display:block;color:var(--ink);font-size:17px;line-height:20px;letter-spacing:1px}
.search{left:748px;top:18px;width:285px;height:28px;background:#f3f4f6;border-radius:3px;font-size:11px;color:var(--muted);padding:6px 12px}
.search svg{position:absolute;right:10px;top:7px}
.socials{display:flex;gap:8px}
.socials i{display:block;border-radius:50%}
.site-header .socials{position:absolute;left:1046px;top:16px}
.site-header .socials i{width:32px;height:32px}

/* nav */
.main-nav{top:96px;height:36px;background:var(--nav);font-size:12px;color:var(--white)}
.main-nav span{position:absolute;top:10px}
.main-nav .active{color:var(--orange)}
.main-nav .active::after{content:"";position:absolute;left:-6px;right:-6px;bottom:-10px;height:2px;background:var(--orange)}
.tagline{left:870px;color:var(--orange)}

/* hero */
.hero{top:132px;height:591px;background:linear-gradient(120deg,#c9c2b8 0%,#9c9791 35%,#6f7478 60%,#3f4146 100%)}
.play{position:absolute;left:558px;top:250px;width:84px;height:84px;border-radius:50%;background:var(--orange);box-shadow:0 0 0 8px rgba(247,147,30,.35)}
.play svg{position:absolute;left:30px;top:24px}

/* what / why */
.about{top:723px;height:792px}
.photo-round{position:absolute;border-radius:50%;border:10px solid var(--white);box-shadow:0 0 0 1px var(--line),0 8px 24px rgba(0,0,0,.08)}
.badge{position:absolute;width:52px;height:52px;border-radius:50%;background:var(--orange);color:var(--white);font-size:24px;font-weight:500;display:flex;align-items:center;justify-content:center}
.about h2{position:absolute;font-size:19px;font-weight:600;color:var(--ink);letter-spacing:.5px}
.about p{position:absolute;font-size:11.5px;line-height:20px;color:var(--text)}

/* features */
.features{top:1515px;height:578px;background:var(--feature-bg)}
.features .eyebrow{left:688px;top:212px;font-size:24px;line-height:28px;color:var(--ink);font-weight:500}
.features h2{position:absolute;left:688px;top:242px;font-size:40px;line-height:48px;font-weight:500;color:var(--ink)}
.features p{position:absolute;left:688px;top:302px;width:300px;font-size:13px;line-height:19px}
.btn-outline{position:absolute;width:154px;height:40px;border:2px solid var(--ink);box-shadow:2px 3px 0 rgba(0,0,0,.15);background:var(--white);color:var(--ink);font-size:13px;font-weight:500;display:flex;align-items:center;justify-content:center}

/* solution */
.solution{top:2093px;height:520px}
.section-title{position:absolute;left:0;width:1200px;text-align:center;color:var(--ink);font-weight:600}
.section-sub{position:absolute;left:0;width:1200px;text-align:center;font-size:12px;color:var(--text)}
.checklist{position:absolute;left:586px;top:188px;width:470px;list-style:none;font-size:12.5px;line-height:20px;color:var(--ink)}
.checklist li{position:relative;padding-left:26px;margin-bottom:12px}
.checklist li::before{content:"";position:absolute;left:0;top:4px;width:12px;height:12px;border:2px solid var(--orange);border-radius:2px}

/* testimonials */
.testimonials{top:2613px;height:457px}
.quote{position:absolute;width:280px;text-align:center}
.quote p{font-size:12px;line-height:20px;padding:0 28px}
.quote .card{height:145px;padding-top:32px}
.quote .card.raised{background:var(--white);box-shadow:0 6px 20px rgba(0,0,0,.12)}
.avatar{width:70px;height:70px;border-radius:50%;margin:-35px auto 0;border:4px solid var(--white);background:linear-gradient(135deg,#d9d2c8,#8d8a86);box-shadow:0 2px 8px rgba(0,0,0,.12)}
.quote strong{display:block;font-size:13px;font-weight:600;color:var(--ink);margin-top:8px}
.quote small{display:block;font-size:10px;color:var(--muted)}
.dots{position:absolute;left:583px;top:418px;display:flex;gap:6px}
.dots i{display:block;width:9px;height:9px;border-radius:50%;background:#dcdfe4}
.dots i:first-child{background:var(--orange)}

/* contact */
.contact{top:3070px;height:545px}
.form-card{position:absolute;left:147px;top:132px;width:653px;height:345px;background:var(--white);box-shadow:0 4px 22px rgba(0,0,0,.1)}
.form-card h3{position:absolute;left:31px;top:30px;font-size:21px;font-weight:600;color:var(--ink)}
.form-card .lead{position:absolute;left:31px;top:60px;font-size:11px}
.field{position:absolute;left:31px;width:279px;height:36px;border:1px solid var(--line);border-radius:3px;font-size:9px;color:var(--muted);padding:11px 12px 0 36px;letter-spacing:.5px}
.field svg{position:absolute;left:12px;top:11px}
.field.filled{color:var(--ink);font-size:12px;padding-top:9px;letter-spacing:0}
.message{position:absolute;left:325px;top:91px;width:290px;height:137px;border:1px solid var(--line);border-radius:3px;font-size:9px;color:var(--muted);padding:12px;letter-spacing:.5px}
.btn-send{position:absolute;left:31px;top:269px;width:155px;height:42px;background:var(--orange);color:var(--white);font-size:10px;display:flex;align-items:center;justify-content:center;letter-spacing:.5px}
.info{position:absolute;left:830px;display:flex;gap:14px;align-items:flex-start}
.info .icon-circle{width:38px;height:38px}
.info b{display:block;font-size:14px;font-weight:500;color:var(--ink);line-height:20px}
.info span{display:block;font-size:12px;color:var(--ink)}

/* footer */
.site-footer{top:3615px;height:190px;background:var(--footer);color:var(--white)}
.site-footer .brand{left:157px;top:62px;font-size:30px}
.site-footer .brand i{width:30px;height:30px}
.foot-nav span{position:absolute;top:76px;font-size:11px}
.foot-nav .active{color:var(--orange)}
.site-footer .socials{position:absolute;left:902px;top:70px}
.site-footer .socials i{width:28px;height:28px;background:var(--white)}
.foot-line{position:absolute;left:147px;top:122px;width:906px;height:1px;background:rgba(255,255,255,.15)}
.copy{position:absolute;left:157px;top:150px;font-size:10px;color:rgba(255,255,255,.55)}
.backtop{position:absolute;left:1005px;top:150px;font-size:10px;color:rgba(255,255,255,.55)}
</style>
</head>
<body>

<div class="topbar">
  <span style="left:35px"><b>Contact</b> – To learn more about the Belvo solution, phone - 9000 1234</span>
  <span style="left:505px"><b>Email</b> – info@belvo.example</span>
  <span style="left:710px"><b>Carers</b> – Ability to access a simple method of quality care</span>
  <span class="lang"><i></i>English ⌄</span>
</div>

<header class="site-header">
  <div class="brand"><i></i>Belvo</div>
  <div class="abs phone-block">
    <div class="icon-circle"><svg width="16" height="16" viewBox="0 0 24 24"><path fill="#fff" d="M6.6 10.8a15 15 0 0 0 6.6 6.6l2.2-2.2c.3-.3.7-.4 1-.2 1.1.4 2.3.6 3.6.6.6 0 1 .4 1 1V20c0 .6-.4 1-1 1A17 17 0 0 1 3 4c0-.6.4-1 1-1h3.5c.6 0 1 .4 1 1 0 1.3.2 2.5.6 3.6.1.3 0 .7-.2 1z"/></svg></div>
    <div><small>Belvo Contact</small><strong>9000 1234</strong></div>
  </div>
  <div class="abs search">Search...
    <svg width="14" height="14" viewBox="0 0 24 24"><circle cx="10" cy="10" r="7" fill="none" stroke="#f7931e" stroke-width="2.5"/><path d="M15 15l6 6" stroke="#f7931e" stroke-width="2.5"/></svg>
  </div>
  <div class="socials"><i style="background:#3b5998"></i><i style="background:#1da1f2"></i><i style="background:var(--orange)"></i></div>
</header>

<nav class="main-nav">
  <span class="active" style="left:35px">Home</span>
  <span style="left:120px">About us</span>
  <span style="left:218px">Our Solution</span>
  <span style="left:337px">Demonstration</span>
  <span style="left:470px">Customer Testimonials</span>
  <span style="left:650px">Contact Us</span>
  <span class="tagline">Easier communication between residents and families</span>
</nav>

<section class="hero" role="img" aria-label="Video still: older couple talking with a care advisor holding a tablet">
  <div class="play"><svg width="30" height="36" viewBox="0 0 30 36"><path d="M0 0L30 18L0 36Z" fill="#fff"/></svg></div>
</section>

<section class="about">
  <svg class="abs" style="left:0;top:0" width="1200" height="792">
    <path d="M414 358 C414 470 470 490 560 520 C650 550 690 560 700 600" fill="none" stroke="#d6dae0" stroke-width="1.5"/>
    <circle cx="700" cy="600" r="4" fill="#c5cad2"/>
  </svg>
  <div class="photo-round" role="img" aria-label="Smiling woman in a meeting" style="left:274px;top:78px;width:280px;height:280px;background:linear-gradient(135deg,#e9e4dc,#b8b2a8 60%,#7a8088)"></div>
  <div class="badge" style="left:306px;top:81px">1</div>
  <h2 style="left:617px;top:150px">WHAT IS Belvo</h2>
  <p style="left:617px;top:182px;width:385px">Belvo is a state-of-the-art solution that provides communication between aged care facilities, residents and families.<br>Belvo has been developed for facilities to augment the best possible care by providing easy, safe and secure communication for families to stay in touch with their loved ones.</p>

  <div class="photo-round" role="img" aria-label="Business team gathered around a document" style="left:700px;top:426px;width:280px;height:280px;background:linear-gradient(135deg,#f1efec,#a9a39c 55%,#5b5f66)"></div>
  <div class="badge" style="left:882px;top:411px">2</div>
  <h2 style="left:470px;top:455px;width:147px;text-align:right">WHY Belvo?</h2>
  <p style="left:190px;top:490px;width:427px;text-align:right">With the spotlight on aged care, facilities need every advantage to demonstrate excellence to residents and their families, and Belvo provide a solution. Reports have been so confronting within the industry that a National Inquiry into Aged Care Standards was created by the Federal Government.<br>There has never been a better time for facilities to update the provision of services through the use of technology.<br>Facilities that already provide quality care can enhance and expand their care for facility management, families and residents.</p>
</section>

<section class="features">
  <div class="abs" role="img" aria-label="Illustration: circle of resident and family portraits around a travel photo" style="left:175px;top:84px;width:400px;height:400px;border-radius:50%;background:radial-gradient(circle,#9fd0ee 0%,#bfe0f4 35%,#e3f0f9 60%,#eef5fb 75%);border:1px solid #d9e4ee"></div>
  <div class="abs icon-circle" style="left:684px;top:128px;width:70px;height:70px">
    <svg width="32" height="32" viewBox="0 0 32 32" fill="none" stroke="#fff" stroke-width="2"><circle cx="16" cy="7" r="3.5"/><circle cx="6" cy="24" r="3.5"/><circle cx="26" cy="24" r="3.5"/><path d="M16 11v6M16 17L6 20M16 17l10 3"/></svg>
  </div>
  <div class="abs eyebrow">Belvo</div>
  <h2>Features</h2>
  <p>There are many variations of passages of Lorem Ipsum available, but the majority have suffered alteration in some form, by injected humour, or randomised words which don't look even slightly believable. If you are going to use a passage of Lorem Ipsum</p>
  <div class="btn-outline" style="left:690px;top:460px">Read More</div>
</section>

<section class="solution">
  <h2 class="section-title" style="top:60px;font-size:27px">Our Solution Belvo Features</h2>
  <p class="section-sub" style="top:110px">Lorem Ipsum is simply dummy text of the printing and typesetting industry. Lorem Ipsum.</p>
  <div class="abs" role="img" aria-label="Smiling woman with an elderly man holding a cane" style="left:63px;top:165px;width:495px;height:330px;background:radial-gradient(ellipse at 50% 45%,#e7d9c9 0%,#c9b8a4 40%,#f4f1ee 72%,#fff 80%)"></div>
  <ul class="checklist">
    <li>Works on all phones and tablets.</li>
    <li>Simple to use.</li>
    <li>Provides frequent resident updates to families such as meal reports, activities and visitors with associated photos and videos.</li>
    <li>Residents privacy is ensured by the use of advanced artificial intelligence processes.</li>
    <li>Belvo complies with the requirements of national privacy law. Information is protected as required by current Australian law.</li>
  </ul>
  <div class="btn-outline" style="left:584px;top:470px">More Features</div>
</section>

<section class="testimonials">
  <h2 class="section-title" style="top:40px;font-size:27px">Testimonial</h2>
  <p class="section-sub" style="top:88px">Lorem Ipsum is simply dummy text of the printing and typesetting industry. Lorem Ipsum.</p>
  <div class="quote" style="left:178px;top:147px">
    <div class="card raised"><p>Lorem Ipsum is simply dummy text of the printing and typesetting industry. Lorem Ipsum.</p></div>
    <div class="avatar" role="img" aria-label="Customer portrait"></div>
    <strong>Jesse T</strong><small>Toronto</small>
  </div>
  <div class="quote" style="left:477px;top:147px">
    <div class="card"><p>Lorem Ipsum is simply dummy text of the printing and typesetting industry. Lorem Ipsum.</p></div>
    <div class="avatar" role="img" aria-label="Customer portrait"></div>
    <strong>Jesse T</strong><small>Toronto</small>
  </div>
  <div class="quote" style="left:773px;top:147px">
    <div class="card"><p>Lorem Ipsum is simply dummy text of the printing and typesetting industry. Lorem Ipsum.</p></div>
    <div class="avatar" role="img" aria-label="Customer portrait"></div>
    <strong>Jesse T</strong><small>Toronto</small>
  </div>
  <div class="dots"><i></i><i></i><i></i><i></i></div>
</section>

<section class="contact">
  <h2 class="section-title" style="top:28px;font-size:34px">Contact Us</h2>
  <p class="section-sub" style="top:80px">There are many variations of passages of Lorem Ipsum available.</p>
  <div class="form-card">
    <h3>Request Call Back.</h3>
    <p class="lead">We are here to answer any question you may have</p>
    <svg class="abs" style="left:578px;top:26px" width="34" height="30" viewBox="0 0 34 30" fill="none" stroke="#b9bec6" stroke-width="1.3"><path d="M2 14L32 2L24 28L16 18Z"/><path d="M16 18L32 2"/></svg>
    <div class="field" style="top:91px"><svg width="12" height="12" viewBox="0 0 12 12" fill="none" stroke="#b9bec6"><circle cx="6" cy="4" r="2.5"/><path d="M1.5 11c0-2.5 2-4 4.5-4s4.5 1.5 4.5 4"/></svg>YOUR NAME *</div>
    <div class="field filled" style="top:142px"><svg width="12" height="12" viewBox="0 0 12 12" fill="none" stroke="#b9bec6"><rect x="1" y="2.5" width="10" height="7"/><path d="M1 2.5l5 4 5-4"/></svg>info@belvo.example</div>
    <div class="field" style="top:192px"><svg width="12" height="12" viewBox="0 0 12 12" fill="none" stroke="#b9bec6"><rect x="3" y="1" width="6" height="10" rx="1"/></svg>MOBILE NO *</div>
    <div class="message">YOUR MESSAGE *</div>
    <div class="btn-send">SEND MESSAGE</div>
  </div>
  <div class="info" style="top:215px">
    <div class="icon-circle"><svg width="16" height="16" viewBox="0 0 12 12" fill="none" stroke="#fff" stroke-width="1.2"><rect x="1" y="2.5" width="10" height="7"/><path d="M1 2.5l5 4 5-4"/></svg></div>
    <div><b>info@belvo.example</b><span>We reply within 24 hours</span></div>
  </div>
  <div class="info" style="top:287px">
    <div class="icon-circle"><svg width="16" height="16" viewBox="0 0 24 24"><path fill="#fff" d="M6.6 10.8a15 15 0 0 0 6.6 6.6l2.2-2.2c.3-.3.7-.4 1-.2 1.1.4 2.3.6 3.6.6.6 0 1 .4 1 1V20c0 .6-.4 1-1 1A17 17 0 0 1 3 4c0-.6.4-1 1-1h3.5c.6 0 1 .4 1 1 0 1.3.2 2.5.6 3.6.1.3 0 .7-.2 1z"/></svg></div>
    <div><b>Have Any Qustion</b><span>9000 1234</span></div>
  </div>
  <div class="info" style="top:358px">
    <div class="icon-circle"><svg width="16" height="16" viewBox="0 0 16 16" fill="none" stroke="#fff" stroke-width="1.3"><circle cx="8" cy="8" r="6.5"/><path d="M1.5 8h13M8 1.5c2 2 2 11 0 13M8 1.5c-2 2-2 11 0 13"/></svg></div>
    <div><b>Website</b><span>www.belvo.example</span></div>
  </div>
</section>

<footer class="site-footer">
  <div class="brand"><i></i>Belvo</div>
  <div class="foot-nav">
    <span class="active" style="left:372px">Home</span>
    <span style="left:452px">About us</span>
    <span style="left:552px">Our Solution</span>
    <span style="left:670px">Demonstration</span>
    <span style="left:803px">Contact Us</span>
  </div>
  <div class="socials"><i></i><i></i><i></i><i></i></div>
  <div class="foot-line"></div>
  <div class="copy">© Copyright Belvo Care 2019</div>
  <div class="backtop">Back Top ⌃</div>
</footer>

</body>
</html>
```